The Corbel Ridge Group's website for high impact furniture promotions

I am looking for a simple website. we are a promotional company that runs events for furniture stores to increase sales for short periods of time. i would like the website to have about 4 areas to explain our company. I would like it to be simple and user friendly. I would like a link to chatterbook and a contact section. I am attaching our logo that i would like somewhere large or possibly in the backround. I am open to different color schemes. I would like to convey fast paced, modern, reliable. I am open to all different styles and look forward to seeing whats out there. we are looking for a quick turn around, so if we see one that we like quick, we will pick that one thanks
Reason: looking for some really creative designs and want to give a fair amount of time to produce
Target Market(s)
Retail Furniture store owners
Industry/Entity Type
It Company
Number of Pages Required
1 page
Colors
Look and feel

```html
<!DOCTYPE html>
<html lang="en">
<head>
<meta charset="utf-8">
<title>The Corbel Ridge Group – High Impact Furniture Promotions</title>
<link href="https://fonts.googleapis.com/css2?family=Raleway:wght@600;700;800;900&family=Lato:ital,wght@0,400;0,700;0,900;1,400&display=swap" rel="stylesheet">
<style>
:root{
  --red:#e8433d;
  --red-dark:#c9322d;
  --navy:#2a3244;
  --navy-deep:#222a3a;
  --ink:#2b2b2b;
  --muted:#6d6f74;
  --mist:#f0f1f3;
  --white:#ffffff;
  --gold:#c9a46a;
}
*{box-sizing:border-box;margin:0;padding:0}
html,body{width:1200px;height:5322px;overflow:hidden}
body{font-family:'Lato',sans-serif;color:var(--ink);background:var(--white);position:relative}
.abs{position:absolute}
h1,h2,h3,.display{font-family:'Raleway',sans-serif}

/* hero */
.hero{position:absolute;left:0;top:0;width:1200px;height:600px}
.hero-photo{position:absolute;inset:0;background:linear-gradient(180deg,#3a3c44 0%,#5b5048 45%,#3b3a3d 100%)}
.hero-shade{position:absolute;inset:0;background:linear-gradient(180deg,rgba(20,24,34,.25),rgba(20,24,34,.45))}
.brand{position:absolute;left:110px;top:28px;width:210px;text-align:center;color:var(--white)}
.brand-dot{width:120px;height:120px;border-radius:50%;background:var(--navy);border:4px solid var(--gold);margin:0 auto 12px}
.brand-name{font-family:'Lato',sans-serif;font-weight:700;font-size:19px;line-height:1.25;color:var(--white)}
.social{display:flex;gap:14px;justify-content:center;margin-top:14px}
.social a{font-size:12px;color:var(--white);text-decoration:none;font-weight:700}
.nav{position:absolute;right:80px;top:40px;display:flex;gap:22px;align-items:center}
.nav a{color:var(--white);font-family:'Lato',sans-serif;font-weight:900;font-size:14px;text-decoration:none;letter-spacing:.3px}
.nav a.cta{background:var(--red);padding:14px 16px}
.hero-title{position:absolute;left:0;width:1200px;top:255px;text-align:center;color:var(--white);font-family:'Raleway',sans-serif;font-weight:900;line-height:1}
.hero-title .l1{display:block;font-size:52px;color:#f2d9c4}
.hero-title .l2{display:block;font-size:76px;margin-top:6px}

/* promotions band */
.promo{position:absolute;left:0;top:600px;width:1200px;height:318px;background:linear-gradient(180deg,#d9463f 0%,#e4554c 55%,#cf3e38 100%);text-align:center;color:var(--white)}
.promo h2{margin-top:112px;font-weight:800;font-size:44px}
.promo .big{display:block;font-family:'Raleway',sans-serif;font-weight:900;font-size:66px;letter-spacing:1px;line-height:1.05}

/* steps */
.steps-title{position:absolute;left:0;width:1200px;top:1035px;text-align:center}
.steps-title .t1{font-family:'Raleway',sans-serif;font-weight:700;font-size:41px;color:var(--ink)}
.steps-title .t2{font-family:'Raleway',sans-serif;font-weight:900;font-size:58px;color:var(--red);line-height:1.15}
.step{position:absolute;top:1225px;width:200px}
.step-ring{width:140px;height:140px;border-radius:50%;border:3px solid var(--red);position:relative;margin-left:2px}
.step-ring svg{position:absolute;left:40px;top:40px}
.step-num{position:absolute;right:-12px;top:-8px;width:40px;height:40px;border-radius:50%;background:var(--red);color:var(--white);font-weight:900;font-size:18px;display:flex;align-items:center;justify-content:center;border:3px solid var(--white)}
.step h3{font-family:'Lato',sans-serif;font-weight:900;font-size:16px;margin-top:20px}
.step p{font-size:15px;line-height:1.45;color:var(--muted);margin-top:4px}
.step-link{position:absolute;top:1270px}

/* showroom */
.showroom{position:absolute;left:0;top:1505px;width:1200px;height:600px}

/* section headings */
.sec-title{position:absolute;left:160px;font-family:'Raleway',sans-serif;font-weight:900;font-size:56px;color:var(--ink);letter-spacing:-.5px}
.sec-title::after{content:"";display:block;width:50px;height:6px;background:var(--red);margin-top:12px}

/* about */
.about-frame{position:absolute;left:1010px;top:2200px;width:190px;height:360px;border:12px solid var(--red);border-right:none}
.about-text{position:absolute;left:160px;top:2340px;width:420px;font-size:15px;line-height:1.75;color:var(--muted)}
.about-text p+p{margin-top:22px}
.about-media{position:absolute;left:640px;top:2300px;width:405px;height:230px;background:linear-gradient(135deg,#e9e5de 0%,#cfd3cc 50%,#8d9a86 100%)}
.play{position:absolute;left:172px;top:85px;width:62px;height:62px;border-radius:50%;background:rgba(255,255,255,.85)}

/* team */
.team{position:absolute;left:0;top:2680px;width:1200px;height:450px;background:var(--mist)}
.slider{position:absolute;top:2770px;display:flex;gap:6px;left:966px}
.slider span{width:32px;height:32px;display:flex;align-items:center;justify-content:center}
.slider .prev{background:#dcdee2}
.slider .next{background:var(--red)}
.member{position:absolute;top:2875px;width:196px}
.member .photo{width:196px;height:196px;background:linear-gradient(160deg,#c9c2ba,#6f6a66)}
.member .photo.hl{outline:8px solid var(--red);outline-offset:-8px}
.member .name{font-family:'Raleway',sans-serif;font-size:20px;font-weight:800;margin-top:12px;color:var(--ink)}
.member .name b{color:var(--red);font-weight:800}
.member .role{font-size:14px;color:var(--muted)}

/* news */
.news{position:absolute;top:3320px;width:262px}
.news .photo{height:142px;background:linear-gradient(150deg,#9a8f84,#4d4742)}
.news .photo.hl{outline:8px solid var(--red);outline-offset:-8px}
.news h3{font-family:'Lato',sans-serif;font-weight:900;font-size:15px;line-height:1.35;margin-top:48px;color:var(--ink)}
.news p{font-size:14px;line-height:1.6;color:var(--muted);margin-top:14px}
.btn{position:absolute;background:var(--red);color:var(--white);font-weight:900;font-size:14px;text-decoration:none;display:flex;align-items:center;gap:8px;justify-content:center}

/* testimonials */
.testi{position:absolute;left:0;top:3940px;width:1200px;height:625px;background:var(--red);color:var(--white);text-align:center}
.testi h2{font-family:'Raleway',sans-serif;font-weight:900;font-size:54px;margin-top:125px}
.testi h2::after{content:"";display:block;width:50px;height:5px;background:var(--white);margin:16px auto 0}
.testi blockquote{width:800px;margin:44px auto 0;font-style:italic;font-size:18px;line-height:2}
.testi .q{font-family:'Raleway',sans-serif;font-style:normal;font-weight:900;font-size:34px;line-height:0;vertical-align:-6px}
.avatar{width:56px;height:56px;border-radius:50%;background:#f5b8b3;margin:30px auto 0}
.testi .who{font-weight:900;font-size:16px;margin-top:12px}
.testi .who-role{font-style:italic;font-size:14px}
.arrow-side{position:absolute;top:4270px}

/* map + footer */
.map{position:absolute;left:0;top:4565px;width:1200px;height:300px;background:linear-gradient(180deg,#eceae5,#e2e0da)}
.footer{position:absolute;left:0;top:4864px;width:1200px;height:458px;background:var(--navy)}
.foot-brand{position:absolute;left:120px;top:4950px;width:240px;text-align:center;color:var(--white)}
.foot-brand .brand-dot{width:150px;height:150px}
.foot-brand .brand-name{font-size:22px}
.contact{position:absolute;left:408px;top:4795px;width:410px;height:527px;background:var(--white);text-align:center}
.contact h2{font-family:'Raleway',sans-serif;font-weight:900;font-size:38px;margin-top:30px;color:var(--ink)}
.contact h2::after{content:"";display:block;width:46px;height:5px;background:var(--red);margin:10px auto 0}
.field{width:222px;margin:0 auto;border-bottom:1px solid #c9cbd0;height:38px;line-height:38px;font-size:14px;color:#7a7c80}
.fields{margin-top:18px}
.contact .btn{position:static;width:112px;height:44px;margin:46px auto 0}
.address{position:absolute;left:818px;top:4955px;width:330px;color:#c9ccd4}
.address h4{font-family:'Lato',sans-serif;font-weight:900;font-size:18px;letter-spacing:1px;color:var(--white)}
.address h4::after{content:"";display:block;width:40px;height:3px;background:var(--red);margin-top:10px}
.addr-row{display:flex;gap:14px;margin-top:22px;font-size:13px;line-height:1.6}
.addr-row strong{color:var(--white)}
.phone{font-size:28px;color:var(--white);font-weight:400}
.foot-social{display:flex;gap:18px;margin-top:34px}
.foot-social a{color:var(--white);text-decoration:none;font-weight:900;font-size:14px}
</style>
</head>
<body>

<header class="hero">
  <div class="hero-photo" role="img" aria-label="Crowd of shoppers queuing outside a furniture store at a sales event"></div>
  <div class="hero-shade"></div>
  <div class="brand">
    <div class="brand-dot"></div>
    <div class="brand-name">The Corbel Ridge Group</div>
    <div class="social"><a href="#">chatterbook</a><a href="#">chirpfeed</a><a href="#">plusring</a><a href="#">linkwork</a></div>
  </div>
  <nav class="nav">
    <a href="#">HOME</a><a href="#">ABOUT</a><a href="#">TRADE SHOW</a><a href="#">SERVICES</a><a href="#">TEAM</a><a href="#">GALLERY</a><a href="#">VIDEOS</a><a href="#">NEWS</a><a class="cta" href="#">CONTACT US</a>
  </nav>
  <h1 class="hero-title"><span class="l1">Let us plan your</span><span class="l2">next BIG event</span></h1>
</header>

<section class="promo" role="img" aria-label="Furniture showroom under a red overlay">
  <h2>High Impact Furniture<span class="big">PROMOTIONS</span></h2>
</section>

<section>
  <div class="steps-title"><div class="t1">Increase sales in</div><div class="t2">4 Easy Steps</div></div>

  <div class="step" style="left:160px">
    <div class="step-ring"><span class="step-num">1</span>
      <svg width="60" height="60" viewBox="0 0 60 60" fill="none" stroke="var(--red)" stroke-width="3"><rect x="8" y="12" width="44" height="40" rx="3"/><line x1="8" y1="22" x2="52" y2="22"/><line x1="20" y1="6" x2="20" y2="16"/><line x1="40" y1="6" x2="40" y2="16"/><g fill="var(--red)" stroke="none"><rect x="15" y="28" width="6" height="6"/><rect x="27" y="28" width="6" height="6"/><rect x="39" y="28" width="6" height="6"/><rect x="15" y="39" width="6" height="6"/><rect x="27" y="39" width="6" height="6"/></g></svg>
    </div>
    <h3>LOREM IPSUM DOLOR</h3><p>Mauris accumsan, purus erat maximus, lorem nulla volutpat diam.</p>
  </div>
  <div class="step" style="left:392px">
    <div class="step-ring"><span class="step-num">2</span>
      <svg width="60" height="60" viewBox="0 0 60 60" fill="none" stroke="var(--red)" stroke-width="3"><path d="M12 30v-8a4 4 0 0 1 4-4h28a4 4 0 0 1 4 4v8"/><rect x="6" y="28" width="8" height="14" rx="3"/><rect x="46" y="28" width="8" height="14" rx="3"/><line x1="14" y1="36" x2="46" y2="36"/><line x1="10" y1="42" x2="10" y2="48"/><line x1="50" y1="42" x2="50" y2="48"/></svg>
    </div>
    <h3>LOREM IPSUM DOLOR</h3><p>Mauris accumsan, purus erat maximus, lorem nulla volutpat diam.</p>
  </div>
  <div class="step" style="left:625px">
    <div class="step-ring"><span class="step-num">3</span>
      <svg width="60" height="60" viewBox="0 0 60 60" fill="var(--red)"><rect x="10" y="38" width="7" height="14"/><rect x="22" y="30" width="7" height="22"/><rect x="34" y="22" width="7" height="30"/><rect x="46" y="14" width="7" height="38"/><path d="M8 30 L24 18 L32 24 L48 8" fill="none" stroke="var(--red)" stroke-width="3"/><path d="M42 6h8v8z"/></svg>
    </div>
    <h3>LOREM IPSUM DOLOR</h3><p>Mauris accumsan, purus erat maximus, lorem nulla volutpat diam.</p>
  </div>
  <div class="step" style="left:862px">
    <div class="step-ring"><span class="step-num">4</span>
      <svg width="60" height="60" viewBox="0 0 60 60" fill="none" stroke="var(--red)" stroke-width="3"><path d="M44 8c-14 2-24 12-28 26l10 10c14-4 24-14 26-28z"/><circle cx="36" cy="24" r="4"/><path d="M16 34l-8 2 6-10h8"/><path d="M26 44l-2 8 10-6v-8"/><path d="M14 46l-6 6"/></svg>
    </div>
    <h3>LOREM IPSUM DOLOR</h3><p>Mauris accumsan, purus erat maximus, lorem nulla volutpat diam.</p>
  </div>
  <svg class="step-link" style="left:322px" width="60" height="30" viewBox="0 0 60 30" fill="none" stroke="#333" stroke-width="2"><path d="M4 26 Q30 -6 56 26"/></svg>
  <svg class="step-link" style="left:556px" width="60" height="30" viewBox="0 0 60 30" fill="none" stroke="#333" stroke-width="2"><path d="M4 26 Q30 -6 56 26"/></svg>
  <svg class="step-link" style="left:790px" width="60" height="30" viewBox="0 0 60 30" fill="none" stroke="#333" stroke-width="2"><path d="M4 26 Q30 -6 56 26"/></svg>
</section>

<svg class="showroom" width="1200" height="600" viewBox="0 0 1200 600" role="img" aria-label="Furniture showroom interior with sofas and armchairs">
  <defs><linearGradient id="room" x1="0" y1="0" x2="0" y2="1"><stop offset="0" stop-color="#5a4a3a"/><stop offset=".5" stop-color="#8a7459"/><stop offset="1" stop-color="#b59f82"/></linearGradient></defs>
  <path d="M0 0H1200V420C880 420 700 470 600 590C500 470 320 420 0 420Z" fill="url(#room)"/>
  <path d="M0 430C320 430 500 480 600 600C700 480 880 430 1200 430" fill="none" stroke="var(--gold)" stroke-width="4"/>
</svg>

<section>
  <h2 class="sec-title" style="top:2220px">ABOUT US</h2>
  <div class="about-frame"></div>
  <div class="about-text">
    <p>Lorem ipsum dolor sit amet, consectetur adipiscing elit. Mauris accumsan, purus vel hendrerit maximus, lorem nulla venenatis elit, vitae volutpat diam ipsum id ligula.</p>
    <p>Duis dolor urna, accumsan a augue et, feugiat sagittis elit. Mauris scelerisque orci vitae dui fermentum, non mollis lectus volutpat. Nullam tincidunt enim lobortis ultricies gravida. Curabitur scelerisque ac tortor eget aliquet. In et ultricies ligula, non lacinia lorem.</p>
  </div>
  <div class="about-media" role="img" aria-label="Bright living room set with grey armchairs and a plant">
    <div class="play"><svg width="62" height="62" viewBox="0 0 62 62"><path d="M25 20v22l18-11z" fill="var(--red)"/></svg></div>
  </div>
</section>

<section class="team"></section>
<h2 class="sec-title" style="top:2745px">OUR TEAM</h2>
<div class="slider">
  <span class="prev"><svg width="10" height="14" viewBox="0 0 10 14"><path d="M8 2L3 7l5 5" fill="none" stroke="#999" stroke-width="2"/></svg></span>
  <span class="next"><svg width="10" height="14" viewBox="0 0 10 14"><path d="M2 2l5 5-5 5" fill="none" stroke="#fff" stroke-width="2"/></svg></span>
</div>
<div class="member" style="left:160px"><div class="photo" role="img" aria-label="Portrait of Rowan Hale"></div><div class="name"><b>Rowan</b> Hale</div><div class="role">Founder &amp; CEO</div></div>
<div class="member" style="left:390px"><div class="photo hl" role="img" aria-label="Portrait of Ines Marlow"></div><div class="name"><b>Ines</b> Marlow</div><div class="role">Co-Founder</div></div>
<div class="member" style="left:628px"><div class="photo" role="img" aria-label="Portrait of Tobias Quell"></div><div class="name"><b>Tobias</b> Quell</div><div class="role">Managing Director</div></div>
<div class="member" style="left:859px"><div class="photo" role="img" aria-label="Portrait of Dorian Vance"></div><div class="name"><b>Dorian</b> Vance</div><div class="role">Advert Manager</div></div>

<section>
  <h2 class="sec-title" style="top:3195px">LATEST NEWS</h2>
  <article class="news" style="left:160px"><div class="photo" role="img" aria-label="Modern furniture gallery with shelving"></div><h3>1 YEAR AGO, WE WERE JUST WRAPPING UP SEASON. NOW WE RULE FRIDAY NIGHTS.</h3><p>Lorem ipsum dolor sit amet, cons adipiscing elit. Mauris accumsan, pure vel hendrerit maximus.</p></article>
  <article class="news" style="left:466px"><div class="photo hl" role="img" aria-label="Dining tables on a showroom floor"></div><h3>1 YEAR AGO, WE WERE JUST WRAPPING UP SEASON. NOW WE RULE FRIDAY NIGHTS.</h3><p>Lorem ipsum dolor sit amet, cons adipiscing elit. Mauris accumsan, pure vel hendrerit maximus.</p></article>
  <article class="news" style="left:774px"><div class="photo" role="img" aria-label="Dining room set with pendant lamps"></div><h3>1 YEAR AGO, WE WERE JUST WRAPPING UP SEASON. NOW WE RULE FRIDAY NIGHTS.</h3><p>Lorem ipsum dolor sit amet, cons adipiscing elit. Mauris accumsan, pure vel hendrerit maximus.</p></article>
  <a class="btn" href="#" style="left:462px;top:3795px;width:226px;height:52px">READ ALL NEWS <svg width="16" height="12" viewBox="0 0 16 12"><path d="M1 6l14-5-5 10-2-4z" fill="#fff"/></svg></a>
</section>

<section class="testi">
  <h2>TESTIMONIALS</h2>
  <blockquote><span class="q">&ldquo;</span> Fusce ut mattis lacus, vel accumsan ligula. Sed cursus diam vel odio pellentes que cursus. Donec augue diam, malesuada ut fringilla convallis, mattis ut neque. Ut eget suscipit enim. Curabitur ullam metus, a tincidunt erat aliquam nec. Suspendisse risus ex, gravida et leo vel, posuere ornare est. <span class="q">&rdquo;</span></blockquote>
  <div class="avatar" role="img" aria-label="Client avatar"></div>
  <div class="who">MILO PENROSE</div><div class="who-role">Client</div>
</section>
<svg class="arrow-side" style="left:110px" width="20" height="36" viewBox="0 0 20 36"><path d="M17 3L3 18l14 15" fill="none" stroke="#f5a7a2" stroke-width="3"/></svg>
<svg class="arrow-side" style="left:1070px" width="20" height="36" viewBox="0 0 20 36"><path d="M3 3l14 15-14 15" fill="none" stroke="#fff" stroke-width="3"/></svg>

<div class="map" role="img" aria-label="Street map of the office area in Raleigh"></div>
<footer class="footer"></footer>
<div class="foot-brand"><div class="brand-dot"></div><div class="brand-name">The Corbel Ridge Group</div></div>

<form class="contact">
  <h2>CONTACT US</h2>
  <div class="fields">
    <div class="field">Enter Your Name</div>
    <div class="field">Enter Your Email</div>
    <div class="field">Enter Your Phone No.</div>
    <div class="field">Subject</div>
    <div class="field">Enter Your Message</div>
  </div>
  <a class="btn" href="#">SUBMIT <svg width="16" height="12" viewBox="0 0 16 12"><path d="M1 6l14-5-5 10-2-4z" fill="#fff"/></svg></a>
</form>

<div class="address">
  <h4>OUR ADDRESS</h4>
  <div class="addr-row"><svg width="14" height="20" viewBox="0 0 14 20"><path d="M7 1a6 6 0 0 0-6 6c0 5 6 12 6 12s6-7 6-12a6 6 0 0 0-6-6z" fill="none" stroke="var(--red)" stroke-width="2"/><circle cx="7" cy="7" r="2" fill="var(--red)"/></svg><div><strong>The Corbel Ridge Group</strong><br>418 Larkspur Lane, Raleigh,<br>North Carolina 27601, United States</div></div>
  <div class="addr-row" style="align-items:center"><svg width="18" height="18" viewBox="0 0 18 18"><path d="M3 1h4l2 4-2 2c1 2 3 4 5 5l2-2 4 2v4c0 1-1 1-2 1C8 17 1 10 1 3c0-1 1-2 2-2z" fill="none" stroke="var(--red)" stroke-width="1.5"/></svg><span class="phone">555 010 0924</span></div>
  <div class="addr-row" style="align-items:center"><svg width="18" height="14" viewBox="0 0 18 14"><rect x="1" y="1" width="16" height="12" fill="none" stroke="var(--red)" stroke-width="1.5"/><path d="M1 1l8 7 8-7" fill="none" stroke="var(--red)" stroke-width="1.5"/></svg><span>hello@corbelridgepromos.com</span></div>
  <div class="foot-social"><a href="#">chatterbook</a><a href="#">chirpfeed</a><a href="#">plusring</a><a href="#">linkwork</a></div>
</div>

</body>
</html>
```